Business Card for: Keelwright Financial Advisory Services Inc.

provide strategic financial advisory services to companies in the areas of corporate finance, mergers and acquisitions, executive coaching and strategic planning

Target Market(s)

Companies, banks, accountants, lawyers

Industry/Entity Type

High end business consulting in corporate finance, mergers and acquisitions, consulting

Contact Information for Business Card

Name of company, Name: xxxxxx xxxxxx , CEO, - phone number: 1-xxx-xxx-xxxx, - email address,

Requirements
Must have
• Must be professional and simple.
Nice to have
• simple, straight graphics, must give the impression that we are trustworthy, professional, competent
Should not have
• loud colors, loud design features

```html
<!DOCTYPE html>
<html lang="en">
<head>
<meta charset="utf-8">
<title>Keelwright Financial – Business Card</title>
<link rel="stylesheet" href="https://fonts.googleapis.com/css2?family=Inter:wght@400;500;700&family=Montserrat:wght@700&display=swap">
<style>
  :root {
    --backdrop: #e4e4e4;
    --card-dark: #121212;
    --card-light: #ffffff;
    --ink: #111111;
    --front-name: #4a4a4a;
  }
  html, body {
    margin: 0;
    padding: 0;
    width: 1200px;
    height: 1200px;
    overflow: hidden;
    background: var(--backdrop);
  }
  .canvas {
    position: relative;
    width: 1200px;
    height: 1200px;
  }
  .card {
    position: absolute;
    left: 179px;
    width: 861px;
    height: 496px;
  }
  .card--front {
    top: 84px;
    background: var(--card-dark);
  }
  .card--back {
    top: 622px;
    background: var(--card-light);
    color: var(--ink);
    font-family: "Inter", sans-serif;
  }
  .front-name {
    position: absolute;
    left: 0;
    right: 0;
    top: 238px;
    margin: 0;
    text-align: center;
    font-family: "Montserrat", sans-serif;
    font-weight: 700;
    font-size: 31px;
    color: var(--front-name);
    line-height: 1;
  }
  .company-name {
    position: absolute;
    left: -12px;
    right: 0;
    top: 116px;
    margin: 0;
    text-align: center;
    font-weight: 700;
    font-size: 40px;
    line-height: 1;
  }
  .person {
    position: absolute;
    left: -18px;
    right: 0;
    top: 270px;
    margin: 0;
    text-align: center;
    font-weight: 500;
    font-size: 29px;
    line-height: 1;
  }
  .contact {
    position: absolute;
    top: 336px;
    left: 0;
    right: 0;
    height: 34px;
    font-size: 26px;
    line-height: 34px;
  }
  .contact span { position: absolute; top: 0; }
  .contact .label { font-weight: 500; font-size: 28px; }
  .contact .label-p { left: 69px; }
  .contact .colon-p { left: 104px; font-weight: 700; }
  .contact .phone { left: 123px; }
  .contact .divider {
    left: 365px;
    top: 2px;
    width: 2px;
    height: 32px;
    background: var(--ink);
  }
  .contact .label-e { left: 415px; }
  .contact .colon-e { left: 453px; font-weight: 700; }
  .contact .email { left: 477px; }
</style>
</head>
<body>
  <main class="canvas">
    <section class="card card--front" aria-label="Card front">
      <p class="front-name">Keelwright Financial Services Inc.</p>
    </section>

    <section class="card card--back" aria-label="Card back">
      <h1 class="company-name">Keelwright Financial Inc.</h1>
      <p class="person">Daniel Harrow - CEO</p>
      <div class="contact">
        <span class="label label-p">P</span>
        <span class="colon-p">:</span>
        <span class="phone">1-xxx-xxx-xxxx</span>
        <span class="divider" aria-hidden="true"></span>
        <span class="label label-e">E</span>
        <span class="colon-e">:</span>
        <span class="email">youremail@yoursite.com</span>
      </div>
    </section>
  </main>
</body>
</html>
```